Business Card Design Project

I am looking for a classy business card design for a product design consultancy. We specialize in Product Design, Prototyping, and Manufacturing Consulting. Products that we design range from consumer electronics to household products all the way to sporting goods. We are based in Arizona and called "Heron Design Works." We like to have fun and goof off as much as we like to create new products. We are young and energetic so we would like our business cards to reflect that. We already have a logo that we would like to implement into the card design. A plain rectangular business card is boring so feel free to get creative, but please, no avocado shaped cards (it's far too literal). Also feel free to play around with textured card stocks or plastic. The final design that we choose will pay attention to all of the little details. Our cards will need to be 2 sided. We're giving you guys free reign to design as you would like. Please have fun with this, it will reflect in our business card.

Thanks guys,
Heron Design Works Team

Industry/Entity Type

Electronics

Requirements
Must have
• We would like to have a spot UV coating somewhere on the business card design if possible.
Nice to have
• Let's see some designs with custom shapes rather than typical rectangular business cards but please no avocado shaped cards, thanks. Also play around with textured card socks.

```html
<!DOCTYPE html>
<html lang="en">
<head>
<meta charset="utf-8">
<title>Heron Design Works – Business Card</title>
<link href="https://fonts.googleapis.com/css2?family=Montserrat:wght@400;500;700&display=swap" rel="stylesheet">
<style>
  :root {
    --backdrop: #e9e7e3;
    --leaf: #7cc242;
    --leaf-deep: #5ea52a;
    --leaf-light: #95d15a;
    --paper: #ffffff;
    --paper-shade: #f1f1f1;
    --ink: #2f2f2f;
    --ink-soft: #555555;
    --rule: #cfcfcf;
  }
  * { box-sizing: border-box; margin: 0; padding: 0; }
  html, body { width: 1200px; height: 900px; overflow: hidden; }
  body {
    background: var(--backdrop);
    font-family: "Montserrat", sans-serif;
    position: relative;
  }
  .card {
    position: absolute;
    border-radius: 22px;
    box-shadow: 0 10px 28px rgba(0,0,0,.18);
    overflow: hidden;
  }
  /* Front */
  .card-front {
    left: 150px; top: 310px;
    width: 520px; height: 300px;
    background: linear-gradient(160deg, var(--leaf-light) 0%, var(--leaf) 45%, var(--leaf-deep) 100%);
  }
  .card-front .sheen {
    position: absolute; inset: 0;
    background: linear-gradient(115deg, rgba(255,255,255,.18) 0%, rgba(255,255,255,0) 40%);
  }
  .front-brand {
    position: absolute; right: 34px; bottom: 34px;
    display: flex; align-items: center; gap: 10px;
    color: var(--paper);
    font-weight: 500; font-size: 26px; letter-spacing: .5px;
  }
  .brand-dot {
    width: 22px; height: 22px; border-radius: 50%;
    background: currentColor; flex: none;
  }
  /* Back */
  .card-back {
    left: 750px; top: 190px;
    width: 300px; height: 520px;
    background: linear-gradient(180deg, var(--paper) 0%, var(--paper-shade) 100%);
    padding: 44px 30px 34px;
    display: flex; flex-direction: column;
  }
  .back-brand {
    display: flex; align-items: center; gap: 8px;
    color: var(--leaf);
    font-weight: 500; font-size: 19px;
  }
  .back-brand .brand-dot { width: 16px; height: 16px; }
  .divider {
    margin-top: 120px;
    border: 0; border-top: 1px solid var(--rule);
  }
  .person-name {
    margin-top: 22px;
    font-weight: 700; font-size: 17px; letter-spacing: .5px;
    color: var(--ink); text-transform: uppercase;
  }
  .person-role {
    font-weight: 500; font-size: 11px; color: var(--leaf);
    margin-top: 2px;
  }
  .phones { margin-top: 18px; font-size: 12px; color: var(--ink-soft); line-height: 1.6; }
  .phones b { color: var(--leaf); font-weight: 700; margin-right: 4px; }
  .web { margin-top: 22px; font-size: 11.5px; color: var(--ink); line-height: 1.6; }
  .social {
    margin-top: auto; align-self: flex-end;
    display: flex; gap: 10px;
  }
  .social span {
    width: 10px; height: 10px; border-radius: 50%;
    background: var(--leaf-deep);
  }
</style>
</head>
<body>
  <section class="card card-front" aria-label="Card front">
    <div class="sheen"></div>
    <div class="front-brand"><span class="brand-dot"></span>Heron Design Works</div>
  </section>

  <section class="card card-back" aria-label="Card back">
    <div class="back-brand"><span class="brand-dot"></span>Heron Design Works</div>
    <hr class="divider">
    <p class="person-name">Dylan Marsh</p>
    <p class="person-role">President</p>
    <p class="phones"><b>P:</b>480 555 0142<br><b>M:</b>602 555 0187</p>
    <p class="web">dylan@herondesignworks.com<br>www.herondesignworks.com</p>
    <div class="social" aria-label="Social profiles"><span></span><span></span><span></span></div>
  </section>
</body>
</html>
```